Payday Lending App Interface Design

Hello, we are building a payday lending application, Lendora, that lend people money. I have drafted some of the screens that show the functionalities we have at the moment, please find the screens in attachments.
The elements in the screens are placed just to show what should be included in those screens, it's not necessary to follow the same layout. If you have better design ideas, you are very welcomed to show off your talent.
I think what we want is a style guide so that we can apply the same style to any screens that are similar to the ones I attached. We really like
the style as in the attached image called Style.png. We might want something similar - a simple, clean design yet fun and engaging. Customised graphical elements such as icons, illustrations are preferable.
Apart from the attached screens, we might also need a design for the On Board screen and the Login/Sign Up screen too.
Our logo colour is in yellow and black. Perhaps we will have a similar colour theme. I also attached the logo file, icon-Lendora.png, if you would like to put it in your design.
Please message me if you need further information.
Regards
Target Market(s)
Young people that doesn't have strong income
Look and feel

```html
<!DOCTYPE html>
<html lang="en">
<head>
<meta charset="utf-8">
<title>Lendora – Revised UI Screens</title>
<link href="https://fonts.googleapis.com/css2?family=Poppins:wght@400;500;600;700&display=swap" rel="stylesheet">
<style>
:root{
  --ink:#0d0d0d;
  --yellow:#fcc000;
  --white:#ffffff;
  --muted:#6f6f6f;
  --field:#f3f3f3;
  --field-line:#e2e2e2;
  --pill:#3b4049;
  --dark-a:#0b0b0c;
  --dark-b:#232a35;
  --text:#1f2a3a;
}
*{box-sizing:border-box;margin:0;padding:0}
html,body{width:1200px;height:2194px;overflow:hidden;background:var(--white)}
body{font-family:"Poppins",sans-serif;color:var(--ink)}
.board{position:absolute;left:0;top:0;width:1412px;height:2581px;transform:scale(.8499);transform-origin:0 0}
.page-title{position:absolute;left:0;width:1412px;top:52px;text-align:center;font-size:42px;font-weight:700;letter-spacing:.3px}
.screen-title{position:absolute;font-size:31px;font-weight:700;white-space:nowrap}
.note{position:absolute;font-size:23.5px;line-height:33px;color:var(--text)}
.note b{display:block;font-weight:700;color:var(--ink);font-size:24px}

/* phone */
.phone{position:absolute;width:262px;height:553px;border:5px solid var(--ink);border-radius:30px;background:var(--white);overflow:hidden}
.phone > *{position:absolute}
.status{left:22px;top:9px;right:18px;display:flex;justify-content:space-between;align-items:center;font-size:9px;font-weight:600;z-index:2}
.status.light{color:var(--white)}
.nav-title{left:0;right:0;text-align:center;font-size:14.5px;font-weight:500}
.back{left:16px;width:12px;height:12px}
.info{left:17px;width:218px;height:48px;background:var(--ink);border-radius:5px;color:var(--white);font-size:8.6px;line-height:13px;display:flex;align-items:center;gap:7px;padding:0 10px}
.info svg{flex:none}
.card{left:17px;width:218px;height:54px;background:var(--white);border-radius:6px;box-shadow:0 2px 10px rgba(0,0,0,.07);display:flex;align-items:center;padding:0 10px;gap:10px}
.card .ico{width:34px;height:34px;border-radius:6px;background:#f0f0f0;display:flex;align-items:center;justify-content:center;flex:none}
.card .lbl{flex:1;font-size:10.5px;font-weight:500;line-height:15px}
.card .lbl small{display:block;font-size:8.6px;font-weight:400;color:var(--muted)}
.dots{width:16px;height:16px;border-radius:50%;background:#eee;display:flex;align-items:center;justify-content:center}
.btn{left:17px;width:218px;height:40px;background:var(--yellow);border-radius:6px;display:flex;align-items:center;justify-content:center;gap:8px;font-size:9.5px;font-weight:600}
.field-lbl{left:26px;font-size:7.5px;font-weight:500;background:var(--white);padding:0 4px;z-index:1;color:#444}
.field{left:17px;width:218px;height:40px;background:var(--field);border:1px solid var(--field-line);border-radius:5px;display:flex;align-items:center;justify-content:space-between;padding:0 12px 0 15px;font-size:9px;color:#555}

/* apply loan */
.hero{left:0;top:0;width:252px;height:199px;background:linear-gradient(180deg,var(--dark-a),var(--dark-b));border-radius:0 0 10px 10px}
.topbar{left:16px;right:14px;top:38px;display:flex;align-items:center;justify-content:space-between;color:var(--white);font-size:14.5px;font-weight:500}
.topbar .acts{display:flex;gap:8px}
.choose{left:0;right:0;top:76px;text-align:center;color:var(--yellow);font-size:9px;font-weight:500}
.amount{left:0;right:0;top:97px;display:flex;justify-content:center;align-items:center;gap:16px;color:var(--white);font-size:22px;font-weight:700}
.amount i{font-style:normal;font-size:17px;font-weight:400}
.max{left:78px;width:97px;top:139px;height:15px;border-radius:8px;background:var(--pill);color:var(--yellow);font-size:7px;text-align:center;line-height:15px;font-weight:500}
.fees{left:17px;width:218px;top:174px;height:84px;border-radius:6px;overflow:hidden;box-shadow:0 2px 10px rgba(0,0,0,.08)}
.fees .row{height:43px;background:var(--white);display:flex;justify-content:space-around;align-items:center;text-align:center;font-size:7px;line-height:13px}
.fees .row b{display:block;font-size:8.6px;font-weight:600}
.fees .total{height:41px;background:var(--ink);color:var(--white);font-size:8.6px;display:flex;align-items:center;justify-content:center}
.term-lbl{left:17px;font-size:8.5px;font-weight:500}
.slider{left:17px;width:218px;height:50px;background:var(--white);box-shadow:0 4px 10px rgba(0,0,0,.05)}
.slider .mark{position:absolute;right:33px;top:7px;font-size:7px}
.slider .track{position:absolute;left:22px;right:10px;top:26px;height:3px;background:var(--ink)}
.slider .fill{position:absolute;left:0;width:143px;top:0;height:3px;background:var(--yellow)}
.slider .knob{position:absolute;top:-7px;width:17px;height:17px;border-radius:50%;background:var(--yellow)}
.agree{left:17px;width:218px;height:44px;background:var(--white);border-radius:6px;box-shadow:0 2px 10px rgba(0,0,0,.07);display:flex;align-items:center;justify-content:space-between;padding:0 14px 0 10px;font-size:8.6px;font-weight:500;line-height:13px}
.agree small{display:block;font-size:7px;font-weight:400;color:var(--muted)}
</style>
</head>
<body>
<svg width="0" height="0" style="position:absolute">
  <defs>
    <symbol id="i-sig" viewBox="0 0 40 10"><rect x="0" y="6" width="2" height="4"/><rect x="3" y="4" width="2" height="6"/><rect x="6" y="2" width="2" height="8"/><rect x="9" y="0" width="2" height="10"/><path d="M15 4a7 7 0 0 1 10 0l-1.2 1.2a5 5 0 0 0-7.6 0zM17.4 6.4a3.4 3.4 0 0 1 5.2 0L20 9z"/><rect x="28" y="2" width="10" height="6" rx="1.5"/><rect x="38.5" y="4" width="1.5" height="2"/></symbol>
    <symbol id="i-back" viewBox="0 0 12 12"><path d="M8 2 4 6l4 4" fill="none" stroke="currentColor" stroke-width="1.6" stroke-linecap="round" stroke-linejoin="round"/></symbol>
    <symbol id="i-info" viewBox="0 0 14 14"><circle cx="7" cy="7" r="6.5" fill="#fff"/><rect x="6.2" y="6" width="1.6" height="4.5" fill="#0d0d0d"/><circle cx="7" cy="4.2" r="0.9" fill="#0d0d0d"/></symbol>
    <symbol id="i-dots" viewBox="0 0 4 12"><circle cx="2" cy="2" r="1.3"/><circle cx="2" cy="6" r="1.3"/><circle cx="2" cy="10" r="1.3"/></symbol>
    <symbol id="i-down" viewBox="0 0 16 16"><circle cx="8" cy="8" r="7" fill="none" stroke="currentColor" stroke-width="1.2"/><path d="M5 7l3 3 3-3" fill="none" stroke="currentColor" stroke-width="1.2" stroke-linecap="round"/></symbol>
    <symbol id="i-eye" viewBox="0 0 16 10"><path d="M8 0C4 0 1 5 1 5s3 5 7 5 7-5 7-5-3-5-7-5z"/><circle cx="8" cy="5" r="2" fill="#f3f3f3"/></symbol>
    <symbol id="i-plus" viewBox="0 0 20 20"><circle cx="10" cy="10" r="10"/><path d="M10 5v10M5 10h10" stroke="#fcc000" stroke-width="2"/></symbol>
    <symbol id="i-shield" viewBox="0 0 18 20"><path d="M9 1 2 4v5c0 5 3 8.5 7 10 4-1.5 7-5 7-10V4z" fill="none" stroke="currentColor" stroke-width="1.6" stroke-linejoin="round"/><path d="m6 10 2.2 2.2L12.5 8" fill="none" stroke="currentColor" stroke-width="1.6" stroke-linecap="round"/></symbol>
    <symbol id="i-menu" viewBox="0 0 20 16"><rect y="1" width="20" height="2" rx="1"/><rect y="7" width="20" height="2" rx="1"/><rect y="13" width="20" height="2" rx="1"/></symbol>
    <symbol id="i-bell" viewBox="0 0 18 18"><path d="M3 13h11l-1.5-2V7a4 4 0 0 0-8 0v4z" fill="#fff"/><circle cx="8.5" cy="15.5" r="1.6" fill="#fff"/><circle cx="14" cy="4" r="3.2" fill="#fcc000"/></symbol>
    <symbol id="i-gear" viewBox="0 0 20 20"><circle cx="10" cy="10" r="7.5" fill="none" stroke="#fff" stroke-width="1.6" stroke-dasharray="3 1.7"/><circle cx="10" cy="10" r="5.5" fill="none" stroke="#fff" stroke-width="1.5"/><circle cx="10" cy="10" r="2.3" fill="none" stroke="#fff" stroke-width="1.5"/></symbol>
    <symbol id="i-cal" viewBox="0 0 18 18"><rect x="1" y="3" width="16" height="14" rx="2"/><rect x="4" y="0.5" width="2" height="4" rx="1"/><rect x="12" y="0.5" width="2" height="4" rx="1"/><rect x="1" y="6.5" width="16" height="1.2" fill="#f0f0f0"/></symbol>
    <symbol id="i-doc" viewBox="0 0 16 20"><path d="M1 1h10l4 4v14H1z" fill="none" stroke="currentColor" stroke-width="1.6" stroke-linejoin="round"/><path d="M4 7h4M4 11h8M4 15h8M10 7h2" stroke="currentColor" stroke-width="1.4"/></symbol>
    <symbol id="i-user" viewBox="0 0 18 18"><circle cx="9" cy="5" r="4"/><path d="M1 17c0-4 3.5-6.5 8-6.5s8 2.5 8 6.5z"/></symbol>
    <symbol id="i-bag" viewBox="0 0 18 20"><path d="M6 1h6l-2 4H8z"/><path d="M7 5h4c4 2 6 6 6 9 0 3-2 5-8 5S1 17 1 14c0-3 2-7 6-9z"/><text x="9" y="16" font-size="8" font-weight="700" text-anchor="middle" fill="#f0f0f0" font-family="Poppins,sans-serif">$</text></symbol>
  </defs>
</svg>

<div class="board">
  <h1 class="page-title">Revised UI Screen</h1>

  <h2 class="screen-title" style="left:97px;top:148px">Bank Details</h2>
  <h2 class="screen-title" style="left:410px;top:148px">Add Bank Acocunt</h2>

  <!-- Bank details -->
  <div class="phone" style="left:66px;top:212px">
    <div class="status"><span>9:41</span><svg width="40" height="10"><use href="#i-sig"/></svg></div>
    <svg class="back" style="top:42px"><use href="#i-back"/></svg>
    <div class="nav-title" style="top:38px">Bank Details</div>
    <div class="info" style="top:75px"><svg width="13" height="13"><use href="#i-info"/></svg><span>We will only transfer money to an account that is in your own name</span></div>
    <div class="card" style="top:142px"><div class="ico"><svg width="16" height="16"><rect width="16" height="16" rx="3" fill="#0d0d0d"/></svg></div><div class="lbl">Harbor Bank<small>11234412</small></div><span class="dots"><svg width="4" height="10"><use href="#i-dots"/></svg></span></div>
    <div class="card" style="top:207px"><div class="ico"><svg width="16" height="16"><circle cx="8" cy="8" r="8" fill="#0d0d0d"/></svg></div><div class="lbl">Payvo<small>12981123</small></div><span class="dots"><svg width="4" height="10"><use href="#i-dots"/></svg></span></div>
    <div class="card" style="top:272px"><div class="ico"><svg width="16" height="16"><rect width="16" height="16" rx="3" fill="#0d0d0d"/></svg></div><div class="lbl">Orchard Pay<small>12981123</small></div><span class="dots"><svg width="4" height="10"><use href="#i-dots"/></svg></span></div>
    <div class="btn" style="top:473px"><svg width="18" height="18"><use href="#i-plus"/></svg>Add Bank Account</div>
  </div>

  <!-- Connect bank -->
  <div class="phone" style="left:430px;top:212px;height:556px">
    <div class="status"><span>9:41</span><svg width="40" height="10"><use href="#i-sig"/></svg></div>
    <svg class="back" style="top:42px"><use href="#i-back"/></svg>
    <div class="nav-title" style="top:38px">Connect Your Bank</div>
    <div class="info" style="top:76px"><svg width="13" height="13"><use href="#i-info"/></svg><span>We will only check bank statements for credit score requirements.</span></div>
    <div class="field-lbl" style="top:150px">Choose Bank</div>
    <div class="field" style="top:155px"><span>Payvo</span><svg width="15" height="15"><use href="#i-down"/></svg></div>
    <div class="field-lbl" style="top:216px">Bank Account Number</div>
    <div class="field" style="top:221px"><span>12981123</span></div>
    <div class="field-lbl" style="top:282px">Password</div>
    <div class="field" style="top:287px"><span>•••••••••</span><svg width="12" height="8"><use href="#i-eye"/></svg></div>
    <div class="btn" style="top:477px"><svg width="16" height="18"><use href="#i-shield"/></svg>Connect Bank Account</div>
  </div>

  <p class="note" style="left:754px;top:210px;width:420px"><b>Revised</b>Only the bank account number and password are required for that page.</p>

  <p class="note" style="left:81px;top:853px;width:1260px"><b>Revised</b>There are 2 versions, with 2 different content.<br><br>1. The card contains a detailed explanation of the interest charged.<br>2. Without a card, only shown the amount of debt that User want to take.<br><br>Both with slider and only Drop Down option (It's up to you which one you want to choose, but to be honest I choose the Drop Down one without the slider because it looks cleaner and more unified.</p>

  <h2 class="screen-title" style="left:82px;top:1175px">Apply Loan v.1</h2>
  <h2 class="screen-title" style="left:420px;top:1175px">Apply Loan v.1</h2>
  <h2 class="screen-title" style="left:755px;top:1175px">Apply Loan v.2</h2>
  <h2 class="screen-title" style="left:1094px;top:1175px">Apply Loan v.2</h2>

  <!-- v1 slider -->
  <div class="phone" style="left:66px;top:1243px">
    <div class="hero"></div>
    <div class="status light"><span>9:41</span><svg width="40" height="10" fill="#fff"><use href="#i-sig"/></svg></div>
    <div class="topbar"><svg width="19" height="15" fill="#fff"><use href="#i-menu"/></svg><span>Apply Loan</span><span class="acts"><svg width="18" height="18"><use href="#i-bell"/></svg><svg width="19" height="19"><use href="#i-gear"/></svg></span></div>
    <div class="choose">Choose Amount</div>
    <div class="amount"><i>‹</i>$ 2,500<i>›</i></div>
    <div class="max">Max $ 5,000</div>
    <div class="fees"><div class="row"><span>Installment Fee (12%)<b>6 x $ 24.99</b></span><span>Admin Fee (0,5%)<b>$ 12.5</b></span></div><div class="total">Installment 6 Months x $ 233.32</div></div>
    <div class="card" style="top:280px"><div class="ico"><svg width="17" height="17"><use href="#i-cal"/></svg></div><div class="lbl">Fortnightly (2 Weeks)<small>Choose Repayment Cycle</small></div><svg width="15" height="15"><use href="#i-down"/></svg></div>
    <div class="term-lbl" style="top:353px">Loan Term</div>
    <div class="slider" style="top:367px"><span class="mark">6 Month</span><div class="track"><div class="fill"></div><span class="knob" style="left:-8px"></span><span class="knob" style="left:135px"></span></div></div>
    <div class="btn" style="top:477px">Next</div>
  </div>

  <!-- v1 dropdown -->
  <div class="phone" style="left:404px;top:1243px">
    <div class="hero"></div>
    <div class="status light"><span>9:41</span><svg width="40" height="10" fill="#fff"><use href="#i-sig"/></svg></div>
    <div class="topbar"><svg width="19" height="15" fill="#fff"><use href="#i-menu"/></svg><span>Apply Loan</span><span class="acts"><svg width="18" height="18"><use href="#i-bell"/></svg><svg width="19" height="19"><use href="#i-gear"/></svg></span></div>
    <div class="choose">Choose Amount</div>
    <div class="amount"><i>‹</i>$ 2,500<i>›</i></div>
    <div class="max">Max $ 5,000</div>
    <div class="fees"><div class="row"><span>Installment Fee (12%)<b>6 x $ 24.99</b></span><span>Admin Fee (0,5%)<b>$ 12.5</b></span></div><div class="total">Installment 6 Months x $ 233.32</div></div>
    <div class="card" style="top:280px"><div class="ico"><svg width="17" height="17"><use href="#i-cal"/></svg></div><div class="lbl">Fortnightly<small>Choose Repayment Cycle</small></div><svg width="15" height="15"><use href="#i-down"/></svg></div>
    <div class="card" style="top:350px"><div class="ico"><svg width="14" height="18"><use href="#i-doc"/></svg></div><div class="lbl">6 Months<small>Choose Loan Term</small></div><svg width="15" height="15"><use href="#i-down"/></svg></div>
    <div class="btn" style="top:476px">Next</div>
  </div>

  <!-- v2 slider -->
  <div class="phone" style="left:743px;top:1243px">
    <div class="hero"></div>
    <div class="status light"><span>9:41</span><svg width="40" height="10" fill="#fff"><use href="#i-sig"/></svg></div>
    <div class="topbar"><svg width="19" height="15" fill="#fff"><use href="#i-menu"/></svg><span>Apply Loan</span><span class="acts"><svg width="18" height="18"><use href="#i-bell"/></svg><svg width="19" height="19"><use href="#i-gear"/></svg></span></div>
    <div class="choose">Choose Amount</div>
    <div class="amount"><i>‹</i>$ 2,500<i>›</i></div>
    <div class="max">Max $ 5,000</div>
    <div class="card" style="top:219px"><div class="ico"><svg width="17" height="17"><use href="#i-cal"/></svg></div><div class="lbl">Fortnightly (2 Weeks)<small>Choose Repayment Cycle</small></div><svg width="15" height="15"><use href="#i-down"/></svg></div>
    <div class="term-lbl" style="top:292px">Loan Term</div>
    <div class="slider" style="top:306px"><span class="mark">6 Month</span><div class="track"><div class="fill"></div><span class="knob" style="left:-8px"></span><span class="knob" style="left:135px"></span></div></div>
    <div class="btn" style="top:476px">Next</div>
  </div>

  <!-- v2 dropdown -->
  <div class="phone" style="left:1083px;top:1243px">
    <div class="hero"></div>
    <div class="status light"><span>9:41</span><svg width="40" height="10" fill="#fff"><use href="#i-sig"/></svg></div>
    <div class="topbar"><svg width="19" height="15" fill="#fff"><use href="#i-menu"/></svg><span>Apply Loan</span><span class="acts"><svg width="18" height="18"><use href="#i-bell"/></svg><svg width="19" height="19"><use href="#i-gear"/></svg></span></div>
    <div class="choose">Choose Amount</div>
    <div class="amount"><i>‹</i>$ 2,500<i>›</i></div>
    <div class="max">Max $ 5,000</div>
    <div class="card" style="top:219px"><div class="ico"><svg width="17" height="17"><use href="#i-cal"/></svg></div><div class="lbl">Fortnightly<small>Choose Repayment Cycle</small></div><svg width="15" height="15"><use href="#i-down"/></svg></div>
    <div class="card" style="top:289px"><div class="ico"><svg width="14" height="18"><use href="#i-doc"/></svg></div><div class="lbl">6 Months<small>Choose Loan Term</small></div><svg width="15" height="15"><use href="#i-down"/></svg></div>
    <div class="btn" style="top:477px">Next</div>
  </div>

  <h2 class="screen-title" style="left:78px;top:1877px">Loan Summary</h2>

  <!-- Loan summary -->
  <div class="phone" style="left:66px;top:1937px">
    <div class="status"><span>9:41</span><svg width="40" height="10"><use href="#i-sig"/></svg></div>
    <svg class="back" style="top:42px"><use href="#i-back"/></svg>
    <div class="nav-title" style="top:38px">Loan Summary</div>
    <div class="card" style="top:75px"><div class="ico"><svg width="17" height="17"><use href="#i-user"/></svg></div><div class="lbl">Application Name<small>Mira Dalton</small></div></div>
    <div class="card" style="top:146px"><div class="ico"><svg width="16" height="18"><use href="#i-bag"/></svg></div><div class="lbl">Loan Amount<small>$ 2,500</small></div></div>
    <div class="card" style="top:217px"><div class="ico"><svg width="17" height="17"><use href="#i-cal"/></svg></div><div class="lbl">Repayment Cycle<small>Fortnightly</small></div></div>
    <div class="card" style="top:288px"><div class="ico"><svg width="14" height="18"><use href="#i-doc"/></svg></div><div class="lbl">Loan Term<small>6 Months</small></div></div>
    <div class="agree" style="top:388px"><span>Loan Agreement<small>Please read before you proceed</small></span><span>›</span></div>
    <div class="btn" style="top:476px">Confirm and Agree</div>
  </div>

  <p class="note" style="left:388px;top:1933px;width:480px"><b>Revised</b>In the wireframe there is a Logo Section which was removed because the space was full and this is enough.</p>
</div>
</body>
</html>
```